New web design for a service provider in the medical field

We are looking for a new design for our website. We are a company that repairs and sells medical endoscopes. Our customers include doctors and hospitals. Our current website can be found at https://lumavend.de/en/lumavend-english.
We need a new web design (without programming) for the following 3 pages:
-Startpage https://lumavend.de/en/lumavend-english/
-Used endoscopes https://lumavend.de/en/used-endoscopes/
-Purchase https://lumavend.de/en/purchase/
The design should be modern and stylish.
The blue color of the logo should be reflected on the page, but not too intrusive.
I have uploaded the images from the header. If more images are needed, let me know and I will upload them.

Target Market(s)
Doctors and hospitals
Coding
Coded - Design and coding required
Number of Pages Required
1 page
Look and feel
Each slider illustrates characteristics of the customer's brand and the style your logo design should communicate.

```html
<!DOCTYPE html>
<html lang="en">
<head>
<meta charset="utf-8">
<title>LumaVend – Endoscope Repair</title>
<link href="https://fonts.googleapis.com/css2?family=Quicksand:wght@500;600;700&family=Lato:wght@400;700;900&display=swap" rel="stylesheet">
<style>
:root{
  --blue:#1a7ad6;
  --blue-dark:#0f5fb3;
  --blue-soft:#b9dcf5;
  --blue-pale:#d9ecfa;
  --ink:#1c1c1c;
  --text:#444;
  --muted:#6b6b6b;
  --navy:#1e2d3a;
  --black:#0b0b0b;
  --white:#fff;
}
*{margin:0;padding:0;box-sizing:border-box}
html,body{width:1200px;height:4441px;overflow:hidden}
body{position:relative;font-family:'Lato',sans-serif;color:var(--text);background:var(--white)}
.abs{position:absolute}
.head{font-family:'Quicksand',sans-serif}
.btn-outline{position:absolute;display:flex;align-items:center;justify-content:center;border:2px solid var(--blue);border-radius:30px;color:var(--blue);font-family:'Lato',sans-serif;font-weight:900;font-size:15px;letter-spacing:.3px;background:transparent}

/* header */
.site-header{position:absolute;left:0;top:0;width:1200px;height:145px;background:var(--white)}
.brand{position:absolute;left:112px;top:48px;display:flex;align-items:center;gap:12px;font-family:'Quicksand',sans-serif;font-weight:700;font-size:30px;color:var(--blue-dark)}
.brand-dot{width:20px;height:20px;border-radius:50%;background:var(--blue)}
.contact{position:absolute;top:14px;display:flex;align-items:center;gap:14px;font-size:15px;color:var(--blue)}
.contact b{color:var(--ink);font-weight:700}
.contact .ic{width:44px;height:44px;border-radius:50%;background:var(--blue);display:flex;align-items:center;justify-content:center}
.main-nav{position:absolute;top:90px;left:374px;display:flex;gap:24px;font-size:14.5px;color:var(--ink)}

/* hero */
.hero{position:absolute;left:0;top:145px;width:1200px;height:690px;background:linear-gradient(100deg,#1a67b8 0%,#3d8fd6 40%,#9cc4e4 70%,#dfe9f1 100%)}
.hero-title{position:absolute;left:110px;top:85px;font-family:'Quicksand',sans-serif;font-weight:700;font-size:62px;line-height:77px;color:var(--white);letter-spacing:1px}
.hero-btn{position:absolute;left:112px;top:415px;width:155px;height:57px;border:2px solid var(--white);border-radius:30px;color:var(--white);font-weight:900;font-size:14.5px;display:flex;align-items:center;justify-content:center}
.hero-wave{position:absolute;left:0;top:735px}

/* about */
.about-title{left:112px;top:912px;width:545px;font-size:30px;line-height:47px;color:var(--ink);font-weight:500}
.about-text{left:112px;top:1075px;width:491px;font-size:15.5px;line-height:25.7px;text-align:justify}
.about-photo{left:664px;top:930px;width:420px;height:420px;border-radius:50%;border:10px solid var(--blue);background:linear-gradient(135deg,#eef3f8,#c7d6e4 60%,#9fb4c8)}

/* brands & services */
.services{position:absolute;left:0;top:1434px;width:1200px;height:699px;background:linear-gradient(180deg,#eef2f5,#e6ebef)}
.tab{position:absolute;top:83px;height:55px;border-radius:30px;display:flex;align-items:center;justify-content:center;color:var(--white);font-weight:900;font-size:15px}
.card{position:absolute;top:209px;width:304px;height:409px;border:1px solid var(--blue-soft);background:rgba(255,255,255,.35);text-align:center}
.card .ring{position:absolute;left:83px;top:21px;width:138px;height:138px;border-radius:50%;background:var(--blue-pale);display:flex;align-items:center;justify-content:center}
.card .ring span{width:104px;height:104px;border-radius:50%;background:var(--blue);display:flex;align-items:center;justify-content:center}
.card h3{position:absolute;top:184px;width:100%;font-family:'Quicksand',sans-serif;font-weight:600;font-size:22px;color:var(--ink)}
.card p{position:absolute;top:228px;left:30px;width:244px;font-size:13px;line-height:26px;color:var(--text)}

/* faulty */
.faulty-photo{left:112px;top:2219px;width:450px;height:386px;border-radius:0 0 110px 0;background:linear-gradient(135deg,#f4f4f4,#b8bcc0 55%,#6c7075)}
.bubble-area{position:absolute;background:radial-gradient(ellipse at center,rgba(185,220,245,.45) 0%,rgba(185,220,245,0) 70%)}

/* outcome */
.outcome{position:absolute;left:0;top:2691px;width:621px;height:547px;background:var(--blue)}
.outcome-photo{position:absolute;left:621px;top:2691px;width:579px;height:547px;background:linear-gradient(135deg,#c9d5de,#8aa9c5 50%,#3e75b4)}
.outcome h2{position:absolute;left:110px;top:58px;font-family:'Quicksand',sans-serif;font-weight:600;font-size:32px;color:var(--white)}
.feat{position:absolute;left:110px;color:var(--white)}
.feat h4{padding-left:34px;font-size:12.5px;font-weight:900;letter-spacing:.2px}
.feat p{padding-left:34px;margin-top:8px;font-size:12.5px;color:#e6f1fb}
.feat svg{position:absolute;left:0;top:-2px}

/* decision */
.decision-title{left:0;top:3318px;width:1200px;text-align:center;font-size:30px;font-weight:500;color:var(--ink)}
.tile{position:absolute;width:276px;text-align:center}
.tile h3{font-family:'Quicksand',sans-serif;font-weight:600;font-size:22px;color:var(--ink);line-height:31px}
.tile p{font-size:13.5px;line-height:26px;color:var(--muted);margin:14px auto 0;width:232px}
.tile .ic{height:80px;display:flex;align-items:flex-end;justify-content:center;margin-bottom:24px}
.tile.active{background:var(--blue)}
.tile.active h3,.tile.active p{color:var(--white)}

/* footer */
.site-footer{position:absolute;left:0;top:4063px;width:1200px;height:378px;background:var(--black);color:var(--white)}
.site-footer h5{position:absolute;top:94px;font-size:20px;font-weight:700;letter-spacing:.3px}
.news{position:absolute;left:110px;top:154px;width:283px;height:47px;border:1px solid #ccc;border-radius:30px}
.news span{position:absolute;left:20px;top:14px;font-size:14px;color:#bbb}
.news b{position:absolute;right:4px;top:4px;width:84px;height:37px;border-radius:20px;background:var(--white);color:var(--ink);font-size:13.5px;display:flex;align-items:center;justify-content:center;font-weight:700}
.links{position:absolute;left:476px;top:150px;font-size:13.5px;line-height:26px}
.co-item{position:absolute;left:686px;display:flex;align-items:center;gap:12px;font-size:13.5px}
.copyright{position:absolute;top:350px;left:0;width:1200px;text-align:center;font-size:13.5px}
</style>
</head>
<body>

<header class="site-header">
  <div class="brand"><span class="brand-dot"></span>LumaVend</div>
  <div class="contact" style="left:520px">
    <span class="ic"><svg width="18" height="18" viewBox="0 0 24 24" fill="#fff"><path d="M6.6 10.8a15 15 0 0 0 6.6 6.6l2.2-2.2c.3-.3.7-.4 1-.2 1.1.4 2.3.6 3.6.6.6 0 1 .4 1 1V20c0 .6-.4 1-1 1A17 17 0 0 1 3 4c0-.6.4-1 1-1h3.5c.6 0 1 .4 1 1 0 1.3.2 2.5.6 3.6.1.3 0 .7-.2 1z"/></svg></span>
    <span>Phone : <b>+49 4100 555 210-0</b></span>
  </div>
  <div class="contact" style="left:828px">
    <span class="ic"><svg width="18" height="14" viewBox="0 0 24 18" fill="#fff"><path d="M0 0h24v3L12 10 0 3zM0 5l12 7 12-7v13H0z"/></svg></span>
    <span>Email : <b>info@lumavend.de</b></span>
  </div>
  <nav class="main-nav">
    <span>Home</span><span>Endoscope Repair</span><span>Used Endoscopes</span><span>Endoscopy Systems</span><span>Endoscopy Accessories</span><span>Purchase</span>
  </nav>
</header>

<section class="hero" role="img" aria-label="Gloved hands in blue holding an endoscope in a clinic">
  <h1 class="hero-title">PUT YOUR<br>ENDOSCOPE<br>IN RELIABLE<br>HANDS!</h1>
  <span class="hero-btn">PURCHASE</span>
  <svg class="abs" style="left:58px;top:320px" width="28" height="48" viewBox="0 0 28 48"><path d="M24 4 6 24l18 20" fill="none" stroke="#fff" stroke-width="5"/></svg>
  <svg class="abs" style="left:1114px;top:320px" width="28" height="48" viewBox="0 0 28 48"><path d="M4 4l18 20L4 44" fill="none" stroke="#fff" stroke-width="5"/></svg>
</section>
<svg class="hero-wave" width="1200" height="100" viewBox="0 0 1200 100">
  <path d="M0 80 C250 110 500 70 750 40 C950 15 1100 30 1200 60 L1200 100 L0 100Z" fill="#fff"/>
  <path d="M0 80 C250 110 500 70 750 40 C950 15 1100 30 1200 60" fill="none" stroke="#1a7ad6" stroke-width="8"/>
</svg>

<h2 class="abs head about-title">Endoscope repairs and second hand endoscopes from LumaVend – cause the outcome matters!</h2>
<p class="abs about-text">LumaVend is a privileged partner for the start-up facility or optimisation of existing healthcare facilities, doctor's offices and hospitals. The quality and reliability of our products and our offered service are our best advertisement! As a result of optimised processes and highly qualified specialists in our company, we can work very quickly and with high quality for your benefit of least possible restrictions in your doctor's office or in your hospital.</p>
<span class="btn-outline" style="left:114px;top:1290px;width:155px;height:57px">LEARN MORE</span>
<div class="abs about-photo" role="img" aria-label="Specialist in a white coat holding an endoscope"></div>

<section class="services">
  <span class="tab" style="left:369px;width:136px;background:var(--navy)">ORVALIS</span>
  <span class="tab" style="left:531px;width:138px;background:var(--blue)">PENTRIX</span>
  <span class="tab" style="left:695px;width:136px;background:var(--navy)">FUJARA</span>

  <div class="card" style="left:112px">
    <div class="ring"><span><svg width="48" height="52" viewBox="0 0 48 52" fill="none" stroke="#fff" stroke-width="2.5"><path d="M8 4h24l8 8v36H8z"/><path d="M14 14h14M14 22h20"/><circle cx="26" cy="34" r="7"/><path d="M31 39l7 7"/></svg></span></div>
    <h3>Repair</h3>
    <p>Manufacturer-independent we repair and maintain endoscopes, individual components (e.g. processors or light</p>
    <span class="btn-outline" style="left:67px;top:325px;width:170px;height:57px">REPAIR REQUEST</span>
  </div>
  <div class="card" style="left:448px">
    <div class="ring"><span><svg width="48" height="52" viewBox="0 0 48 52" fill="none" stroke="#fff" stroke-width="2.5"><path d="M8 4h24l8 8v36H8z"/><path d="M14 14h14M14 22h20"/><circle cx="26" cy="34" r="7"/><path d="M31 39l7 7"/></svg></span></div>
    <h3>Sale</h3>
    <p>Manufacturer-independent we repair and maintain endoscopes, individual components (e.g. processors or light</p>
    <span class="btn-outline" style="left:72px;top:325px;width:200px;height:57px">PURCHASE REQUEST</span>
  </div>
  <div class="card" style="left:784px">
    <div class="ring"><span><svg width="48" height="52" viewBox="0 0 48 52" fill="none" stroke="#fff" stroke-width="2.5"><path d="M8 4h24l8 8v36H8z"/><path d="M14 14h14M14 22h20"/><circle cx="26" cy="34" r="7"/><path d="M31 39l7 7"/></svg></span></div>
    <h3>Purchase</h3>
    <p>Manufacturer-independent we repair and maintain endoscopes, individual components (e.g. processors or light</p>
    <span class="btn-outline" style="left:74px;top:325px;width:155px;height:57px">SELL DEVICE</span>
  </div>
</section>

<div class="abs faulty-photo" role="img" aria-label="Endoscope control body mounted on a holder"></div>
<div class="bubble-area" style="left:640px;top:2470px;width:520px;height:190px" role="img" aria-label="Decorative scattered light blue bubbles"></div>
<h2 class="abs head" style="left:679px;top:2282px;font-size:32px;font-weight:500;color:var(--ink)">Faulty Endoscope?</h2>
<p class="abs" style="left:679px;top:2347px;font-size:14.5px;color:var(--text)">We ensure quick and smooth repairs!</p>
<p class="abs" style="left:679px;top:2389px;font-size:14.5px;color:var(--text)">Simple place a</p>
<span class="btn-outline" style="left:679px;top:2448px;width:164px;height:55px">PICK-UP ORDER</span>

<section class="outcome">
  <h2>Cause The Outcome Matters!</h2>
  <div class="feat" style="top:133px"><svg width="20" height="20" viewBox="0 0 20 20"><circle cx="10" cy="10" r="8" fill="none" stroke="#cfe6fa" stroke-width="2"/><path d="M6 10l3 3 6-6" fill="none" stroke="#cfe6fa" stroke-width="2"/></svg><h4>ONE COMPANY FOR EVERYONE</h4><p>We are a service provider for doctors and hospitals!</p></div>
  <div class="feat" style="top:195px"><svg width="20" height="20" viewBox="0 0 20 20"><circle cx="10" cy="10" r="8" fill="none" stroke="#cfe6fa" stroke-width="2"/><path d="M6 10l3 3 6-6" fill="none" stroke="#cfe6fa" stroke-width="2"/></svg><h4>EXPERIENCE CHARACTERISES US</h4><p>Our team has many years of experience in the business field!</p></div>
  <div class="feat" style="top:257px"><svg width="20" height="20" viewBox="0 0 20 20"><circle cx="10" cy="10" r="8" fill="none" stroke="#cfe6fa" stroke-width="2"/><path d="M6 10l3 3 6-6" fill="none" stroke="#cfe6fa" stroke-width="2"/></svg><h4>THE PRODUCT IS CLOSE TO OUR HEARTS</h4><p>We repair and sell second hand, flexible endoscopes!</p></div>
  <div class="feat" style="top:319px"><svg width="20" height="20" viewBox="0 0 20 20"><circle cx="10" cy="10" r="8" fill="none" stroke="#cfe6fa" stroke-width="2"/><path d="M6 10l3 3 6-6" fill="none" stroke="#cfe6fa" stroke-width="2"/></svg><h4>GUARANTEED SERVICE</h4><p>You receive a six-month warranty on all repairs!</p></div>
  <div class="feat" style="top:381px"><svg width="20" height="20" viewBox="0 0 20 20"><circle cx="10" cy="10" r="8" fill="none" stroke="#cfe6fa" stroke-width="2"/><path d="M6 10l3 3 6-6" fill="none" stroke="#cfe6fa" stroke-width="2"/></svg><h4>QUALITY NOT QUANTITY</h4><p>Reliability and durability instead of inferior replacements!</p></div>
  <div class="feat" style="top:443px"><svg width="20" height="20" viewBox="0 0 20 20"><circle cx="10" cy="10" r="8" fill="none" stroke="#cfe6fa" stroke-width="2"/><path d="M6 10l3 3 6-6" fill="none" stroke="#cfe6fa" stroke-width="2"/></svg><h4>SERVICES FOR EVERYONE</h4><p>Our service includes the manufacturers Orvalis, Pentrix and Fujara!</p></div>
</section>
<div class="outcome-photo" role="img" aria-label="Gloved hand holding an endoscope handpiece"></div>

<h2 class="abs head decision-title">LumaVend GmbH, your decision for your future</h2>

<div class="bubble-area" style="left:1060px;top:3490px;width:140px;height:130px" role="img" aria-label="Decorative scattered light blue bubbles"></div>
<div class="bubble-area" style="left:160px;top:3930px;width:320px;height:130px" role="img" aria-label="Decorative scattered light blue bubbles"></div>

<div class="tile" style="left:119px;top:3420px">
  <div class="ic"><svg width="66" height="66" viewBox="0 0 66 66" fill="none" stroke="#1a7ad6" stroke-width="4"><circle cx="33" cy="33" r="29"/><path d="M33 16v18l11 8"/></svg></div>
  <h3>Fast repairs</h3>
  <p>Keep potential disruptions in your doctor's office or in your hospital at minimum as a result of</p>
</div>
<div class="tile active" style="left:462px;top:3410px;height:305px;padding-top:10px">
  <div class="ic"><svg width="70" height="66" viewBox="0 0 70 66" fill="none" stroke="#fff" stroke-width="4"><path d="M5 32 35 5l30 27M12 26v36h16V42h14v20h16V26"/></svg></div>
  <h3>On-site service</h3>
  <p>We will gladly pay you a visit to to carry out analysis and repairs on site. Due to our many years of</p>
</div>
<div class="tile" style="left:803px;top:3420px">
  <div class="ic"><svg width="74" height="74" viewBox="0 0 74 74" fill="none" stroke="#1a7ad6" stroke-width="3.5"><circle cx="37" cy="37" r="22"/><path d="M37 6v9M37 59v9M6 37h9M59 37h9M15 15l6 6M53 53l6 6M15 59l6-6M53 21l6-6"/><path d="M31 26v14l6 4 6-4V26M37 44v14"/></svg></div>
  <h3>Without a maintenance contract</h3>
  <p>No subscription or other maintenance contract, but</p>
</div>

<div class="tile" style="left:119px;top:3732px">
  <div class="ic"><svg width="80" height="80" viewBox="0 0 80 80" fill="none" stroke="#1a7ad6" stroke-width="3"><path d="M30 8h20l-6 12H36z"/><path d="M36 20c-14 8-18 22-14 32h36c4-10 0-24-14-32"/><text x="40" y="46" font-family="Lato,sans-serif" font-size="18" font-weight="700" fill="#1a7ad6" stroke="none" text-anchor="middle">$</text><path d="M6 60l14-4c6 0 10 4 16 4h12M6 70l18 4 30-10 18-14"/></svg></div>
  <h3>Highly cost efficient</h3>
  <p>Benefit from our first class recommendations and implementation by our</p>
</div>
<div class="tile" style="left:462px;top:3732px">
  <div class="ic"><svg width="80" height="80" viewBox="0 0 80 80" fill="none" stroke="#1a7ad6" stroke-width="3"><path d="M14 6h34l10 10v58H14z"/><text x="30" y="34" font-family="Lato,sans-serif" font-size="20" font-weight="700" fill="#1a7ad6" stroke="none">$</text><path d="M22 46h20M22 56h16M22 66h26M74 26 48 60l-6 4 2-7 26-34z"/></svg></div>
  <h3>Loan equipment service</h3>
  <p>Use our service of high-quality loan devices during the downtime of your defective endoscope</p>
</div>
<div class="tile" style="left:803px;top:3732px">
  <div class="ic"><svg width="80" height="80" viewBox="0 0 80 80" fill="none" stroke="#1a7ad6" stroke-width="3"><circle cx="40" cy="30" r="22"/><circle cx="40" cy="30" r="15"/><path d="M38 24l4-3v18"/><path d="M6 66h20l-4-8h36l-4 8h20l-6-6 6-6H52M28 54H12l6 6"/></svg></div>
  <h3>First class service</h3>
  <p>Our clients always come first!</p>
</div>

<footer class="site-footer">
  <h5 style="left:112px">NEWSLETTER SIGN UP</h5>
  <div class="news"><span>Your Email</span><b>SUBMIT</b></div>

  <h5 style="left:476px">QUICK LINKS</h5>
  <div class="links">Home<br>Endoscope Repair<br>Used Endoscopes<br>Endoscopy Systems<br>Endoscopy Accessories<br>Purchase</div>

  <h5 style="left:686px">COMPANY</h5>
  <div class="co-item" style="top:160px"><svg width="14" height="18" viewBox="0 0 14 18" fill="#fff"><path d="M7 0a7 7 0 0 0-7 7c0 5 7 11 7 11s7-6 7-11a7 7 0 0 0-7-7zm0 10a3 3 0 1 1 0-6 3 3 0 0 1 0 6z"/></svg>Lorem ipsum dolor sit</div>
  <div class="co-item" style="top:199px"><svg width="16" height="16" viewBox="0 0 24 24" fill="#fff"><path d="M6.6 10.8a15 15 0 0 0 6.6 6.6l2.2-2.2c.3-.3.7-.4 1-.2 1.1.4 2.3.6 3.6.6.6 0 1 .4 1 1V20c0 .6-.4 1-1 1A17 17 0 0 1 3 4c0-.6.4-1 1-1h3.5c.6 0 1 .4 1 1 0 1.3.2 2.5.6 3.6.1.3 0 .7-.2 1z"/></svg>+1 (888) 888 8888</div>
  <div class="co-item" style="top:238px"><svg width="17" height="13" viewBox="0 0 24 18" fill="#fff"><path d="M0 0h24v3L12 10 0 3zM0 5l12 7 12-7v13H0z"/></svg>info@lumavend.com</div>

  <h5 style="left:910px">SOCIAL MEDIA</h5>
  <span class="abs" style="left:944px;top:155px;width:20px;height:20px;border-radius:50%;background:#fff"></span>
  <span class="abs" style="left:986px;top:155px;width:20px;height:20px;border-radius:50%;border:2px solid #fff"></span>

  <p class="copyright">©Copyrights 2022 lumavend &nbsp;&nbsp;|&nbsp;&nbsp; All Rights Reserved</p>
</footer>

</body>
</html>
```